"Word Cloud" lists of countries, by decade, who have adopted women's suffrage

The winning designer will (eventually, but not necessarily within this project--see "Nice to Haves", below) design a total of eight images, based on the eight lists of countries (see attached files) in order, by decade, that they adopted women's suffrage.

One of the the attached images is a screen shot of five pages of the book KITE: Notes Toward a Borderless Tomorrow, showing how these lists are presently arranged on 6"x9" pages.

We essentially want to spice up these 8 lists and make them more fun to look at, for the reader.

Target Market(s)

General audience. People who want to make a difference. People who want to do something to change the world, and want to read a book about how we can actually do it.

Industry/Entity Type

Political

Font styles to use
Serif
Sans Serif
Decorative
Script

Requirements
Must have
• At least two initial designs, one for each of the two largest lists (lists 5 and 6). All country names must be spelled correctly. A WORD doc has been provided with all the text you need to work with. An EXAMPLE word cloud has been provided for inspiration. The look and feel of these "Country Clouds" wants to go all over the place, but all names should be (at least somewhat) readable.
• IMPORTANT ELEMENTS: (1) There are a few places where current countries were just one, when they got women's suffrage. Keep this info intact, together, in the cloud. EXAMPLE (from list 6):
•  British Leeward Islands (remove ", including today’s:", but keep together with)
•  Antigua and Barbuda
•  British Virgin Islands
•  Montserrat
•  Saint Kitts and Nevis
•  Anguilla
• (2) The names of the countries should stay in roughly the same order as found in the lists, but laid out (very) roughly right to left and then top to bottom, loosely akin to the standard flow of text written in the latin alphabet. It is fine to alter this standard in minor ways to achieve a better look to the design. Just don't move a country found at the top of one list into the middle of that list or down to the bottom, etc.
• These country clouds will be printed in black and white, so keep the designs greyscale.
• These "country clouds" should be 4.5" in width.The largest country clouds, with the most countries found in them, should not exceed 6" in length.
Nice to have
• (Eventually) all 8 lists in the form of "Country Clouds"---that are playful, but with serious elements. Pull up a list of countries by population, have the 20 biggest use the biggest font sizes. Use many different fonts, mix it up! Essentially, these 8 lists all want to become word clouds, with each nation's full name as its own "word." See example cloud.
• Though having all 8 lists in clouds at the end of this project is "nice to have," the winner for this design might simply produce 2 such clouds, along with a cost estimate attached to the submitted design for what they would charge to complete the other 6 clouds.
Should not have
• Do NOT include the textual transitions found between the lists, in the screen shot or word doc. They are there just to help you see how the different graphics will be used and what will go either before or after them.
• No need to use bullet points.

```html
<!DOCTYPE html>
<html lang="en">
<head>
<meta charset="utf-8">
<title>Country Cloud</title>
<link rel="stylesheet" href="https://fonts.googleapis.com/css2?family=Abril+Fatface&family=Alfa+Slab+One&family=Archivo+Black&family=Audiowide&family=Cinzel:wght@700&family=Cinzel+Decorative&family=Cormorant+Garamond:ital,wght@1,500&family=Cormorant+SC:wght@500&family=Courgette&family=Josefin+Slab:wght@600&family=Montserrat:wght@400;800&family=Old+Standard+TT&family=Oswald:wght@300;500;600&family=Playfair+Display:wght@600&family=Space+Mono&family=Special+Elite&family=Stardos+Stencil:wght@700&display=swap">
<style>
  :root {
    --bg-center: #ffffff;
    --bg-edge: #dedede;
    --ink-black: #222222;
    --ink-dark: #3f3f3f;
    --ink-mid: #595959;
    --ink-grey: #7a7a7a;
    --ink-soft: #959595;
    --ink-pale: #b8b8b8;
    --outline-fill: #f2f2f2;
  }
  html, body {
    margin: 0;
    padding: 0;
    overflow: hidden;
  }
  .canvas {
    width: 985px;
    height: 1200px;
    background: radial-gradient(ellipse at 50% 50%, var(--bg-center) 0%, #f1f1f1 45%, var(--bg-edge) 100%);
  }
  .cloud { display: block; width: 985px; height: 1200px; }
  .country { dominant-baseline: alphabetic; }

  .armenia     { font-family: "Alfa Slab One", serif; font-size: 84px; fill: var(--ink-mid); }
  .canada      { font-family: "Oswald", sans-serif; font-weight: 300; font-size: 142px; fill: var(--outline-fill); stroke: var(--ink-grey); stroke-width: 2; }
  .estonia     { font-family: "Cormorant Garamond", serif; font-style: italic; font-weight: 500; font-size: 64px; fill: var(--ink-soft); }
  .latvia      { font-family: "Special Elite", serif; font-size: 68px; fill: var(--ink-soft); }
  .russia      { font-family: "Stardos Stencil", serif; font-weight: 700; font-size: 64px; fill: var(--ink-black); }
  .uruguay     { font-family: "Archivo Black", sans-serif; font-size: 96px; fill: var(--ink-grey); }
  .georgia     { font-family: "Oswald", sans-serif; font-weight: 600; font-size: 68px; fill: var(--ink-soft); }
  .netherlands { font-family: "Old Standard TT", serif; font-size: 62px; fill: var(--ink-mid); }
  .ireland     { font-family: "Alfa Slab One", serif; font-size: 44px; fill: var(--ink-mid); }
  .azerbaijan  { font-family: "Audiowide", sans-serif; font-size: 56px; fill: var(--ink-soft); }
  .hungary     { font-family: "Oswald", sans-serif; font-weight: 300; font-size: 50px; fill: var(--ink-pale); }
  .germany     { font-family: "Playfair Display", serif; font-weight: 600; font-size: 124px; fill: var(--ink-dark); }
  .kyrgyzstan  { font-family: "Cormorant SC", serif; font-weight: 500; font-size: 46px; fill: var(--ink-mid); }
  .lithuania   { font-family: "Josefin Slab", serif; font-weight: 600; font-size: 50px; fill: var(--ink-soft); }
  .uk          { font-family: "Cinzel", serif; font-weight: 700; font-size: 64px; fill: var(--ink-dark); }
  .poland      { font-family: "Abril Fatface", serif; font-size: 54px; fill: var(--ink-black); }
  .austria     { font-family: "Montserrat", sans-serif; font-weight: 400; font-size: 74px; fill: var(--ink-soft); }
  .belarus     { font-family: "Space Mono", monospace; font-size: 52px; fill: var(--ink-soft); }
  .belgium     { font-family: "Cormorant SC", serif; font-weight: 500; font-size: 42px; fill: var(--ink-mid); }
  .jersey      { font-family: "Oswald", sans-serif; font-weight: 500; font-size: 58px; fill: var(--ink-grey); }
  .luxembourg  { font-family: "Montserrat", sans-serif; font-weight: 800; font-size: 56px; fill: var(--ink-mid); }
  .ukraine     { font-family: "Cinzel Decorative", serif; font-size: 88px; fill: var(--ink-pale); }
  .zimbabwe    { font-family: "Courgette", cursive; font-size: 56px; fill: var(--ink-black); }
</style>
</head>
<body>
<main class="canvas">
  <svg class="cloud" viewBox="0 0 985 1200" xmlns="http://www.w3.org/2000/svg" aria-label="Countries that adopted women's suffrage">
    <text class="country armenia" x="214" y="188" textLength="426" lengthAdjust="spacingAndGlyphs">ARMENIA</text>

    <text class="country canada" x="142" y="312" textLength="388" lengthAdjust="spacingAndGlyphs">CANADA</text>
    <text class="country estonia" x="534" y="254" textLength="262" lengthAdjust="spacingAndGlyphs">Estonia</text>
    <text class="country latvia" x="549" y="320" textLength="297" lengthAdjust="spacingAndGlyphs">LATVIA</text>

    <text class="country netherlands" transform="translate(172,884) rotate(-90)" textLength="548" lengthAdjust="spacingAndGlyphs">NETHERLANDS</text>

    <text class="country russia" x="189" y="392" textLength="673" lengthAdjust="spacingAndGlyphs">RUSSIAN REPUBLIC</text>
    <text class="country uruguay" x="189" y="478" textLength="435" lengthAdjust="spacingAndGlyphs">URUGUAY</text>
    <text class="country georgia" x="646" y="468" textLength="220" lengthAdjust="spacingAndGlyphs">GEORGIA</text>

    <text class="country ireland" transform="translate(190,496) rotate(90)" textLength="260" lengthAdjust="spacingAndGlyphs">IRELAND</text>
    <text class="country azerbaijan" x="254" y="544" textLength="554" lengthAdjust="spacingAndGlyphs">AZERBAIJAN</text>
    <text class="country hungary" transform="translate(832,496) rotate(90)" textLength="188" lengthAdjust="spacingAndGlyphs">HUNGARY</text>

    <text class="country germany" x="238" y="648" textLength="572" lengthAdjust="spacingAndGlyphs">GERMANY</text>
    <text class="country kyrgyzstan" x="240" y="696" textLength="310" lengthAdjust="spacingAndGlyphs">Kyrgyzstan</text>
    <text class="country lithuania" x="578" y="698" textLength="208" lengthAdjust="spacingAndGlyphs">Lithuania</text>
    <text class="country uk" x="238" y="760" textLength="586" lengthAdjust="spacingAndGlyphs">United Kingdom</text>

    <text class="country poland" transform="translate(832,716) rotate(90)" textLength="240" lengthAdjust="spacingAndGlyphs">POLAND</text>

    <text class="country austria" x="188" y="832" textLength="324" lengthAdjust="spacingAndGlyphs">AUSTRIA</text>
    <text class="country belarus" x="544" y="834" textLength="260" lengthAdjust="spacingAndGlyphs">Belarus</text>
    <text class="country belgium" x="186" y="882" textLength="156" lengthAdjust="spacingAndGlyphs">Belgium</text>
    <text class="country jersey" transform="translate(382,1080) rotate(-90)" textLength="228" lengthAdjust="spacingAndGlyphs">JERSEY</text>
    <text class="country luxembourg" x="392" y="894" textLength="412" lengthAdjust="spacingAndGlyphs">LUXEMBOURG</text>
    <text class="country ukraine" x="392" y="976" textLength="376" lengthAdjust="spacingAndGlyphs">UKRAINE</text>
    <text class="country zimbabwe" x="392" y="1040" textLength="270" lengthAdjust="spacingAndGlyphs">Zimbabwe</text>
  </svg>
</main>
</body>
</html>
```